Consulting company with focus on aviation needs

We need a new business card design for our company. The company consults with multiple players in the industry like manufacturers and airlines. It is also a supplier and an inter-company level. Given the targeted industry (aviation) it should be both kind of serious, sound, secure, classy, ​​but also a bit technical, innovative. Should not be too playful, however, "fresh", "airy", "ligth" and "suprising" are suitabe attributes. The existing logo shall be used.

Airlines

```html
<!DOCTYPE html>
<html lang="en">
<head>
<meta charset="utf-8">
<title>NORVANE Business Card</title>
<link href="https://fonts.googleapis.com/css2?family=Questrial&display=swap" rel="stylesheet">
<style>
  :root {
    --stage: #d4d4d4;
    --card: #231f20;
    --card-glow: #2e2a2b;
    --accent-brown: #4a3526;
    --accent-teal: #2bb5a0;
    --accent-green: #a6ce5b;
    --accent-orange: #f5a623;
    --brand-grey: #8d8f91;
    --ink-light: #f2f2f2;
  }
  * { margin: 0; padding: 0; box-sizing: border-box; }
  html, body { width: 1200px; height: 1200px; overflow: hidden; background: var(--stage); }
  body { font-family: "Questrial", "Century Gothic", sans-serif; color: var(--ink-light); }

  .card {
    position: absolute;
    left: 180px;
    width: 840px;
    height: 480px;
    background: var(--card);
    overflow: hidden;
    box-shadow: 0 14px 30px rgba(0,0,0,0.25);
  }
  .card--back { top: 90px; }
  .card--front { top: 630px; }

  .card__backdrop {
    position: absolute;
    left: -120px; top: -160px;
    width: 560px; height: 560px;
    border-radius: 50%;
    background: radial-gradient(circle at 60% 55%, var(--accent-brown) 0%, var(--card-glow) 55%, var(--card) 75%);
    opacity: 0.8;
  }

  .brand { position: absolute; display: flex; flex-direction: column; align-items: flex-end; }
  .brand__row { display: flex; align-items: center; gap: 18px; }
  .brand__name { color: var(--brand-grey); letter-spacing: 0.28em; line-height: 1; }
  .brand__dot { border-radius: 50%; background: var(--accent-teal); }
  .brand__tagline { color: var(--accent-orange); letter-spacing: 0.04em; margin-top: 8px; }

  .card--back .brand { left: 250px; top: 175px; }
  .card--back .brand__name { font-size: 64px; }
  .card--back .brand__dot { width: 74px; height: 74px; }
  .card--back .brand__tagline { font-size: 22px; }

  .card--front .brand { right: 60px; top: 120px; }
  .card--front .brand__name { font-size: 44px; }
  .card--front .brand__dot { width: 52px; height: 52px; }
  .card--front .brand__tagline { font-size: 16px; }

  .person { position: absolute; left: 60px; top: 56px; }
  .person__name { color: var(--accent-green); font-size: 30px; letter-spacing: 0.02em; }
  .person__role { font-size: 20px; margin-top: 4px; }

  .divider {
    position: absolute; left: 60px; right: 60px; top: 250px;
    height: 2px; background: var(--accent-teal);
  }

  .address { position: absolute; left: 60px; top: 272px; font-size: 20px; line-height: 1.4; font-style: normal; }
  .address__web { color: var(--accent-green); }

  .contact { position: absolute; right: 60px; bottom: 52px; list-style: none; font-size: 22px; line-height: 1.45; }
  .contact__item { display: flex; align-items: center; justify-content: flex-end; gap: 12px; }
  .contact__icon { width: 18px; height: 18px; flex: none; }
</style>
</head>
<body>
  <section class="card card--back">
    <div class="card__backdrop" role="img" aria-label="Faint decorative curves in warm brown tones"></div>
    <div class="brand">
      <div class="brand__row">
        <span class="brand__name">NORVANE</span>
        <span class="brand__dot"></span>
      </div>
      <span class="brand__tagline">Guiding Fleets - Shaping Skyways</span>
    </div>
  </section>

  <section class="card card--front">
    <div class="card__backdrop" role="img" aria-label="Faint decorative curves in warm brown tones"></div>
    <div class="person">
      <p class="person__name">MARLA QUINT</p>
      <p class="person__role">Manager</p>
    </div>
    <div class="brand">
      <div class="brand__row">
        <span class="brand__name">NORVANE</span>
        <span class="brand__dot"></span>
      </div>
      <span class="brand__tagline">Guiding Fleets - Shaping Skyways</span>
    </div>
    <div class="divider"></div>
    <address class="address">
      <p>418 Harbour Lane Suite 205</p>
      <p>Ashford ON K2M 4R7</p>
      <p class="address__web">www.norvane.com</p>
    </address>
    <ul class="contact">
      <li class="contact__item">(555) 014 2280
        <svg class="contact__icon" viewBox="0 0 18 18"><rect x="4" y="1" width="10" height="16" rx="2" fill="none" stroke="var(--accent-green)" stroke-width="1.6"/><circle cx="9" cy="14" r="1" fill="var(--accent-green)"/></svg>
      </li>
      <li class="contact__item">(555) 014 2281
        <svg class="contact__icon" viewBox="0 0 18 18"><path d="M4 2 L7 2 L8 6 L6 7.5 Q8 11 10.5 12 L12 10 L16 11 L16 14 Q16 16 14 16 Q3 14 2 4 Q2 2 4 2 Z" fill="var(--accent-green)"/></svg>
      </li>
      <li class="contact__item">hello@norvane.com
        <svg class="contact__icon" viewBox="0 0 18 18"><rect x="1.5" y="4" width="15" height="10" fill="none" stroke="var(--accent-green)" stroke-width="1.6"/><path d="M1.5 4 L9 10 L16.5 4" fill="none" stroke="var(--accent-green)" stroke-width="1.6"/></svg>
      </li>
    </ul>
  </section>
</body>
</html>
```